WP website design (Brisko)

We need a wordpress design that will incorporate a professional color scheme with company logo in a clean layout. The design needs to consider that this will be developed on a responsive theme. Colors are that of the logo and and an accent color (perhaps light brown/tan). Client wants a 'modern' look.

Industry/Entity Type

It Company

Font styles to use
Serif
Sans Serif

Colors

Designer to choose colors to be used in the design.

Requirements
Must have
• Must Have:
- Navigation: 1) Home 2) Real Estate Listings 3) Auctions 4) Buyers 5) Sellers 6) Services 7) Meet the Crew 8) Contact Us

Site will have a slideshow element (image attached) and the following widgets: 1) Featured Auctions 2) Testimonials blog widget 3) 'Auction Alerts' email sign up 4) FB Chirper RSS.

In the footer, there will be smaller company logo, the affiliations logo, and contact info below:
Brisko Auctions & Realty, Inc.
58391 Corvan Hollow Road • Suite 604 • Orlando, FL 32899
Office: 407.555.0148 / Cell: 407.555.0193 / Fax: 407.555.0176
Email: info@briskoauctions.example
Nice to have
• - - Site will have drop-down menus - please indicate the styling, for instance the dropdown menus 1) Upcoming Auctions 2) Past Auctions under the 'Auctions' link

```html
<!DOCTYPE html>
<html lang="en">
<head>
<meta charset="utf-8">
<title>Brisko Auctions &amp; Realty</title>
<link href="https://fonts.googleapis.com/css2?family=Questrial&display=swap" rel="stylesheet">
<style>
:root{
  --red:#a3242b;
  --red-dark:#7e1b21;
  --brown:#8f5431;
  --panel:#f0f0f0;
  --line:#dcdcdc;
  --text:#3c3c3c;
  --white:#fff;
  --slate:#3d3d3d;
}
*{box-sizing:border-box;margin:0;padding:0}
html,body{width:818px;height:1200px;overflow:hidden}
body{position:relative;background:var(--white);font-family:"Questrial",Arial,sans-serif;color:var(--text);font-size:8.4px;line-height:1.75}
.abs{position:absolute}

/* header */
.brand{left:52px;top:10px;color:var(--red);font-size:38px;line-height:1;letter-spacing:-1px}
.brand small{display:block;font-size:12px;letter-spacing:7px;margin:4px 0 0 14px}
.search{right:50px;top:32px;display:flex;align-items:center;gap:8px}
.search-label{color:var(--red);font-size:9px}
.search-box{width:130px;height:21px;border:1px solid #ccc;display:flex;align-items:center;justify-content:space-between;padding-left:7px;color:#999;font-size:8px}
.search-btn{width:19px;height:19px;background:#111;display:flex;align-items:center;justify-content:center}

/* nav */
.nav{left:0;top:81px;width:818px;height:31px;background:var(--brown);display:flex;padding-left:50px}
.nav a{color:var(--white);text-decoration:none;font-size:9.6px;height:31px;display:flex;align-items:center;padding:0 16px;margin-right:1px}
.nav a.active{background:var(--red)}
.nav a:nth-child(n+2){padding:0 16.6px}

/* slider */
.slider{left:50px;top:120px;width:472px;height:274px;border:3px solid #ddd;background:linear-gradient(180deg,#7fa9cf 0%,#c2d4e3 30%,#9ea7a8 45%,#3f5a2c 70%,#b5aca1 100%)}
.dots{position:absolute;left:260px;bottom:11px;display:flex;gap:4px}
.dots span{width:9px;height:9px;border-radius:50%;background:#fff}
.dots span:first-child{background:var(--red)}

/* featured */
.featured{left:50px;top:410px;width:473px;height:604px;background:var(--panel);border-radius:3px;padding:10px 8px}
.featured h2{font-weight:400;color:var(--red);font-size:16px;line-height:1;margin:3px 0 9px 2px}
.card{background:var(--white);border:1px solid var(--line);margin-bottom:9px}
.card-head{height:24px;line-height:24px;padding-left:9px;font-size:11.5px;color:var(--brown);background:linear-gradient(#fff,#f2f2f2);border-bottom:1px solid var(--line)}
.card-body{display:flex;padding:11px 9px 0 9px}
.thumb{width:118px;height:106px;flex:none;border:1px solid #ccc}
.thumb.one{background:linear-gradient(180deg,#7da3d2 0%,#c9d7e6 35%,#e8e4de 55%,#5f7b45 85%)}
.thumb.two{background:linear-gradient(180deg,#8fb2d9 0%,#a47f6b 40%,#8a5a44 65%,#5e7a43 90%)}
.info{padding-left:12px}
.info h3{font-weight:400;color:var(--red);font-size:13px;line-height:1;margin:0 0 4px}
.btns{display:flex;gap:6px;margin:10px 0 0 -4px}
.btn{height:23px;padding:0 16px;display:flex;align-items:center;color:var(--white);font-size:8.4px;border-radius:2px}
.btn.details{background:var(--brown)}
.btn.photos{background:var(--red)}
.btn.videos{background:var(--slate)}
.live{margin:11px 9px 8px 12px;border:1px solid var(--line);background:#f7f7f7;padding:6px 11px 5px;display:flex;justify-content:space-between;align-items:center;font-size:7.8px;line-height:2}
.live h4{font-weight:400;color:var(--red);font-size:12.5px;line-height:1.2;margin-bottom:2px}
.live b{font-weight:400;color:var(--brown)}
.bid{background:var(--brown);color:var(--white);height:26px;padding:0 11px;display:flex;align-items:center;border-radius:2px;font-size:8.2px;margin-top:-22px}
.pager{position:absolute;left:8px;top:560px;height:24px;padding:0 12px;border:1px solid var(--line);background:var(--white);display:flex;align-items:center;font-size:8px;gap:8px}
.powered{position:absolute;right:10px;top:553px;width:121px;height:38px;border:1px solid #ccc;border-radius:4px;background:var(--white)}
.powered span{position:absolute;left:8px;top:8px;width:104px;height:20px;border-radius:3px;background:#dfe6ef}

/* sidebar */
.widget{left:542px;width:226px;border:1px solid var(--line);background:var(--panel);border-radius:2px}
.widget h2{background:var(--red);color:var(--white);font-weight:400;font-size:12.5px;height:26px;line-height:26px;padding-left:12px}
.alerts{top:122px;height:92px}
.alerts .field{margin:10px 12px 7px;height:24px;background:var(--white);border:1px solid #ccc;padding-left:8px;line-height:23px;color:#888;font-size:8px}
.alerts .sign{margin-left:153px;width:59px;height:18px;background:var(--brown);color:var(--white);font-size:7.8px;display:flex;align-items:center;justify-content:center;border-radius:2px}
.testi{top:226px;height:277px}
.quote{margin:0 13px;padding:10px 0 8px;border-bottom:1px solid var(--line);font-style:italic;font-size:8.4px;line-height:1.72}
.quote:last-of-type{border-bottom:0}
.quote .mark{display:inline-block;vertical-align:top;margin-right:4px;margin-top:1px}
.quote .by{color:var(--brown);margin-top:6px}
.readall{margin:1px 0 0 69px;width:143px;height:28px;background:var(--brown);color:var(--white);display:flex;align-items:center;justify-content:center;font-size:8.4px;border-radius:2px}
.connect{top:513px;height:126px}
.connect ul{list-style:none;margin:0 13px}
.connect li{height:30px;display:flex;align-items:center;gap:8px;border-bottom:1px solid var(--line);font-size:8.6px}
.connect li:last-child{border-bottom:0}
.connect i{width:20px;height:20px;border-radius:50%;display:block}

/* footer */
.footer{left:0;top:1035px;width:818px;height:131px;background:var(--red);color:var(--white)}
.footer h2{font-weight:400;font-size:11.5px;line-height:1}
.contact-title{position:absolute;left:50px;top:18px}
.foot-brand{position:absolute;left:50px;top:38px;font-size:20px;line-height:1}
.address{position:absolute;left:50px;top:72px;font-size:7.9px;line-height:1.6}
.phones{position:absolute;left:205px;top:34px;font-size:7.9px;line-height:1.85}
.aff-title{position:absolute;left:472px;top:18px}
.badge{position:absolute;top:42px;background:rgba(255,255,255,.18)}
.copy{left:0;top:1166px;width:818px;height:34px;background:var(--red-dark);color:#c98a8d;font-size:7.6px;display:flex;align-items:center;justify-content:center}
</style>
</head>
<body>

<header>
  <div class="abs brand">Brisko<small>AUCTIONS</small></div>
  <div class="abs search">
    <span class="search-label">Auction Search</span>
    <div class="search-box">Search Here..
      <span class="search-btn"><svg width="9" height="9" viewBox="0 0 10 10"><circle cx="4" cy="4" r="3" fill="none" stroke="#fff" stroke-width="1.5"/><line x1="6.2" y1="6.2" x2="9.3" y2="9.3" stroke="#fff" stroke-width="1.6"/></svg></span>
    </div>
  </div>
</header>

<nav class="abs nav">
  <a class="active">HOME</a><a>REAL ESTATE LISTINGS</a><a>AUCTIONS</a><a>BUYERS</a><a>SELLERS</a><a>SERVICES</a><a>MEET THE CREW</a><a>CONTACT US</a>
</nav>

<div class="abs slider" role="img" aria-label="Slideshow photo of a white stucco home with arched entry, palm trees and paver driveway">
  <div class="dots"><span></span><span></span><span></span><span></span></div>
</div>

<section class="abs featured">
  <h2>Featured Auctions</h2>

  <article class="card">
    <div class="card-head">Real Estate Auction</div>
    <div class="card-body">
      <div class="thumb one" role="img" aria-label="Photo of a large white residential home with columned entry"></div>
      <div class="info">
        <h3>Residential Home</h3>
        <p>Aliquam molestie, mi et imperdiet euismod, dui purus auctor tellus, et interdum lacus lectus et ante. Sed accumsan sollicitudin sapien, sit amet adipiscing turpis gravida ac. In congue, neque ac lobortis volutpat, libero mauris varius mi, vitae suscipit ipsum ligula vitae risus.</p>
        <div class="btns"><span class="btn details">DETAILS</span><span class="btn photos">PHOTOS</span></div>
      </div>
    </div>
    <div class="live">
      <div>
        <h4>Live On-Site Auction</h4>
        <div><b>Began:</b> Saturday, October 05, 2013 at 10:00 AM EDT</div>
        <div><b>Location:</b> 1742 Marlow Crescent</div>
        <div>Kestrel Falls, OH 43999</div>
      </div>
      <span class="bid">CLICK HERE FOR ONLINE BIDDING</span>
    </div>
  </article>

  <article class="card">
    <div class="card-head">Real Estate Auction</div>
    <div class="card-body">
      <div class="thumb two" role="img" aria-label="Photo of a brick two-storey family home"></div>
      <div class="info">
        <h3>Residential Home</h3>
        <p>Aliquam molestie, mi et imperdiet euismod, dui purus auctor tellus, et interdum lacus lectus et ante. Sed accumsan sollicitudin sapien, sit amet adipiscing turpis gravida ac. In congue, neque ac lobortis volutpat, libero mauris varius mi, vitae suscipit ipsum ligula vitae risus.</p>
        <div class="btns"><span class="btn details">DETAILS</span><span class="btn photos">PHOTOS</span><span class="btn videos">VIDEOS</span></div>
      </div>
    </div>
    <div class="live">
      <div>
        <h4>Live On-Site Auction</h4>
        <div><b>Began:</b> Saturday, October 05, 2013 at 10:00 AM EDT</div>
        <div><b>Location:</b> 1742 Marlow Crescent</div>
        <div>Kestrel Falls, OH 43999</div>
      </div>
      <span class="bid">CLICK HERE FOR ONLINE BIDDING</span>
    </div>
  </article>

  <div class="pager">&laquo; PREV <span>|</span> NEXT &raquo;</div>
  <div class="powered" role="img" aria-label="Auction platform partner badge"><span></span></div>
</section>

<aside>
  <div class="abs widget alerts">
    <h2>Auction Alerts</h2>
    <div class="field">Enter Email Address</div>
    <div class="sign">SIGN UP</div>
  </div>

  <div class="abs widget testi">
    <h2>Testimonials</h2>
    <div class="quote">
      <svg class="mark" width="18" height="11" viewBox="0 0 18 11"><circle cx="4" cy="6" r="4" fill="#bbb"/><circle cx="13" cy="6" r="4" fill="#bbb"/></svg>Aliquam molestie, mi et imperdiet euismod, dui purus auctor tellus, et interdum lacus lectus et ante. Sed accumsan sollicitudin sapien, sit amet adipiscing turpis gravida ac....
      <div class="by">-Dara Whitlow</div>
    </div>
    <div class="quote">
      <svg class="mark" width="18" height="11" viewBox="0 0 18 11"><circle cx="4" cy="6" r="4" fill="#bbb"/><circle cx="13" cy="6" r="4" fill="#bbb"/></svg>Aliquam molestie, mi et imperdiet euismod, dui purus auctor tellus, et interdum lacus lectus et ante. Sed accumsan sollicitudin sapien, sit amet adipiscing turpis gravida ac....
      <div class="by">-Dara Whitlow</div>
    </div>
    <div class="readall">READ ALL TESTIMONIALS</div>
  </div>

  <div class="abs widget connect">
    <h2>Connect us</h2>
    <ul>
      <li><i style="background:#3b5a98"></i>Socialpage</li>
      <li><i style="background:#2a9fd8"></i>Chirper</li>
      <li><i style="background:#f3901d"></i>Rss Feeds</li>
    </ul>
  </div>
</aside>

<footer class="abs footer">
  <h2 class="contact-title">Contact Info</h2>
  <div class="foot-brand">Brisko</div>
  <div class="address">Brisko Auctions &amp; Realty, Inc.<br>58391 Corvan Hollow Road<br>Suite 604 • Orlando,<br>FL 32899</div>
  <div class="phones">Office: 407.555.0148<br>Cell: 407.555.0193<br>Fax: 407.555.0176<br>Email: info@briskoauctions.example</div>
  <h2 class="aff-title">Affiliations with</h2>
  <div class="badge" style="left:478px;width:74px;height:52px;border-radius:4px" role="img" aria-label="State association affiliation badge"></div>
  <div class="badge" style="left:570px;width:43px;height:48px" role="img" aria-label="National association affiliation badge"></div>
  <div class="badge" style="left:628px;width:88px;height:34px;top:48px" role="img" aria-label="Accreditation affiliation badge"></div>
  <div class="badge" style="left:733px;width:37px;height:42px" role="img" aria-label="Professional membership badge"></div>
</footer>
<div class="abs copy">Copyright © 2014 All Right Reserved &nbsp;|&nbsp; Privacy Policy</div>

</body>
</html>
```